QR82 Computer Produced for Poultry Houses needs a Corporate Touch

We need a unique screen design with unique graphics for our new product called "QR82". QR82 product is a computer produced for poultry houses. It has a LED screen on which user can change settings for heating, air quaility, inside temprateure, cooling, pressure etc as defined in the attached pictures.

We need 6 designs for the following :

1- QR82 BOX Front Cover Design
2- LED Screen Main Menu
3- LED Screen Inner Menu
4- LED Screen Main Page Menu
5- Vector Logo (JPEG is included, will be prepared in vectorel format)
6- Stationery Design

Explanations are defined below:

1- QR82 BOX Front Cover Design: This box is 37cm width and 47 cm height. It has a LED screen (19 cm x 14cm) in the middle and 3 circular buttons under the LED screen as seenin the attachment. We need a simple but good quality design including corporate colors (dark blue and red) for this box only for the front face of the box.

Attached pictures : 1-a.jpg 1-b.jpg 1-c.jpg (example)

2- LED Screen Main Menu : LED screen (8.7 cm x 15.5 cm) and a border. This menu includes 12 main menu buttons. You will design 12 menu buttons. This menu should look like tabrelo start menu or mivant menu with icons.
a- Values
b- Air Conditioning
c- Heating
d- Alarm
e- Fans
f- Cooling
g-Pressure
h-Timing
i- Reports
j- Close Lights
k- Weights
l- Management (Admin)

Attached pictures : 2-a.jpg 2-b.jpg LEDDimensions.jpg

3- LED Screen Inner Menu : This screen is one example inner menu when clicked on one of icons defined in (2). You will design up and down arrows, textbox and "Go to back" button and "Go to Home" button and final screen design (placement)

Attached pictures : 3-a.jpg

4- LED Screen Main Page Menu : This menu has a poultry house drawing with summary information boxes above.

You will submit the main page design.

Additionally, We need 3 GIF pictures with animation (defined in 4-a.jpg)
a- Moving fans (turning)
b- Fire (burning)
c- Pets (dropping wet drops down on the pad - brown rectangular area)
Attached pictures : 4-a.jpg

Poultry house has 10 fans all in one row. and 6 fans on the long side.

5- Vector logo : In this part, you will submit 2 vectorel logos. First, you will design Vectorel format of dalvera_logo.png (attached) and PNG format. And will design QR82 logo with same structure, fonts, puntos.

6- Stationery Design : Cardvisit + Letter design + Company headed paper

Industry/Entity Type

Computer

Colors
0456a4
ef363c
add136

Requirements
Nice to have
• Flat design, best user experience

```html
<!DOCTYPE html>
<html lang="en">
<head>
<meta charset="utf-8">
<title>dalvera – Letterhead</title>
<link rel="stylesheet" href="https://fonts.googleapis.com/css2?family=Carlito:wght@400;700&display=swap">
<style>
  :root {
    --brand-blue: #2b3a8f;
    --brand-red: #e8333b;
    --ink: #1a1a1a;
    --paper: #ffffff;
  }
  html, body {
    margin: 0;
    padding: 0;
    width: 800px;
    height: 1200px;
    overflow: hidden;
    background: var(--paper);
  }
  .letterhead {
    position: relative;
    width: 800px;
    height: 1200px;
    background: var(--paper);
    font-family: "Carlito", "Calibri", sans-serif;
    color: var(--ink);
  }
  .brand {
    position: absolute;
    left: 48px;
    top: 88px;
    display: flex;
    align-items: center;
    gap: 8px;
  }
  .brand-mark {
    width: 34px;
    height: 34px;
    background: var(--brand-blue);
  }
  .brand-name {
    font-size: 36px;
    font-weight: 700;
    color: var(--brand-blue);
    line-height: 1;
    letter-spacing: 0.5px;
  }
  .header-rule {
    position: absolute;
    left: 72px;
    top: 126px;
    width: 728px;
    height: 10px;
  }
  .website {
    position: absolute;
    right: 48px;
    top: 139px;
    font-size: 12px;
    font-weight: 700;
    color: var(--brand-red);
  }
  .letter-body {
    position: absolute;
    left: 48px;
    top: 204px;
    width: 708px;
    font-size: 14px;
    line-height: 19.4px;
  }
  .letter-body p { margin: 0; }
  .footer-rule {
    position: absolute;
    left: 48px;
    top: 1140px;
    width: 705px;
    height: 1.5px;
    background: var(--brand-red);
  }
  .contacts {
    position: absolute;
    right: 96px;
    top: 1150px;
    display: flex;
    gap: 22px;
    font-size: 9.5px;
    color: var(--brand-red);
  }
  .contact {
    display: flex;
    align-items: center;
    gap: 5px;
  }
  .contact svg { width: 10px; height: 10px; }
</style>
</head>
<body>
<main class="letterhead">
  <header>
    <div class="brand">
      <span class="brand-mark"></span>
      <span class="brand-name">dalvera</span>
    </div>
    <svg class="header-rule" viewBox="0 0 728 10" preserveAspectRatio="none">
      <defs>
        <linearGradient id="ruleFade" x1="0" x2="1" y1="0" y2="0">
          <stop offset="0" stop-color="#e8333b"/>
          <stop offset="0.45" stop-color="#ee5a60"/>
          <stop offset="1" stop-color="#e8333b" stop-opacity="0"/>
        </linearGradient>
      </defs>
      <path d="M0 9 C 120 6, 400 3, 728 2 L728 4 C 400 5, 120 8, 0 10 Z" fill="url(#ruleFade)"/>
    </svg>
    <div class="website">www.dalveraelektrik.com.tr</div>
  </header>

  <section class="letter-body">
    <p>Dear</p>
    <p>Adit venis ad ut ommolorum eum asinihi lluptintur seriaspiet a qui consequam alit harcia vidus, tem et ulparum essitas velit molut magnis estis exernatatque vollut quaeceatur? Quidem. Solorehenda veligenihil maio. Cus assiti beaque consed mo de et ommolup tatur, officiur?</p>
    <p>Fero et faccaborest aspictorume nonsequ assequatem intemporerat que con raepero mo beaquos as aliamus amentum consequi a que doloria epuditis eaque con non cupti re cus debit rehenihit magnit quosapicim seque voluptatem quae in periati aessin cus aut ut illecusam evenihillati doluptatium del ium lautemp erferrum, tetum alibuscim non cullorit que pre nobita nonsed quat alibusant.</p>
    <p>Non repudis dolupta sectotat aut fugia dolupti totatur eperore pedion et volorrum rescillupta nes molupta­ta eturi que pro totaerem ra non reperit, si rescillab illecatat aut experibus arum ressumquos maximillor sinveniatem aut is atinven discipis alis venda dunt.</p>
  </section>

  <footer>
    <div class="footer-rule"></div>
    <div class="contacts">
      <span class="contact">
        <svg viewBox="0 0 10 10" aria-hidden="true"><circle cx="5" cy="5" r="5" fill="#e8333b"/><path d="M3.2 2.6 L4.2 3.6 L3.8 4.3 Q4.6 5.6 5.7 6.2 L6.4 5.8 L7.4 6.8 L6.7 7.5 Q4.5 7.2 2.6 3.3 Z" fill="#fff"/></svg>
        222334455667788
      </span>
      <span class="contact">
        <svg viewBox="0 0 10 10" aria-hidden="true"><circle cx="5" cy="5" r="5" fill="#e8333b"/><rect x="2.6" y="3.4" width="4.8" height="3.2" fill="#fff"/><path d="M2.6 3.4 L5 5.2 L7.4 3.4" stroke="#e8333b" stroke-width="0.6" fill="none"/></svg>
        email@dalveraelektrik.com.tr
      </span>
    </div>
  </footer>
</main>
</body>
</html>
```